Facebook Ad

I am looking for an ad for my moving company that highlights are long distance moving service. I want the ad to also mention the we give free in-home quotes. Also Ithe ad will have a call no action at the bottom so it will not need a phone number but I would like nice picture.

```html
<!DOCTYPE html>
<html lang="en">
<head>
<meta charset="utf-8">
<title>Harlow Moving – Long-Distance Moving Ad</title>
<link rel="stylesheet" href="https://fonts.googleapis.com/css2?family=Montserrat:wght@700;800&family=Roboto:wght@400;500;700&display=swap">
<style>
  :root {
    --stage-edge: #7f86a0;
    --stage-center: #b4b8c8;
    --card-bg: #ffffff;
    --text-main: #1c1e21;
    --text-muted: #65676b;
    --link-bg: #f0f2f5;
    --button-bg: #e4e6eb;
    --divider: #dadde1;
    --accent: #f26a21;
    --headline: #ffffff;
    --avatar: #2f5aa8;
  }
  * { box-sizing: border-box; margin: 0; padding: 0; }
  html, body { width: 737px; height: 1200px; overflow: hidden; }
  body {
    background: radial-gradient(ellipse at center, var(--stage-center) 0%, var(--stage-edge) 100%);
    font-family: "Roboto", Arial, sans-serif;
    color: var(--text-main);
    position: relative;
  }
  .ad-post {
    position: absolute;
    left: 22px; top: 22px;
    width: 693px; height: 1156px;
    background: var(--card-bg);
    box-shadow: 0 2px 10px rgba(0,0,0,0.25);
    display: flex; flex-direction: column;
  }
  .post-header { height: 220px; padding: 18px 26px 0; position: relative; }
  .author { display: flex; align-items: center; gap: 17px; }
  .author-avatar {
    width: 70px; height: 70px; border-radius: 50%;
    background: var(--avatar);
    border: 2px solid var(--divider);
  }
  .author-name { font-size: 28px; font-weight: 500; line-height: 1.2; }
  .author-meta { font-size: 23px; color: var(--text-muted); margin-top: 2px; }
  .more-menu { position: absolute; right: 26px; top: 28px; }
  .post-text { font-size: 27px; line-height: 38px; margin-top: 30px; }

  .ad-visual {
    height: 619px; position: relative;
    background: linear-gradient(180deg,
      #c9c9c4 0%, #8c9184 14%, #55604c 30%, #6f7268 44%,
      #9a9a96 52%, #b7b7b3 60%, #8e8c88 70%, #4b4035 82%, #3a2e22 100%);
  }
  .ad-headline {
    position: absolute; left: 0; right: 0; top: 100px;
    text-align: center;
    font-family: "Montserrat", Arial, sans-serif;
    font-weight: 800; font-size: 51px; line-height: 64px;
    letter-spacing: 2px; color: var(--headline);
    text-shadow: 0 2px 6px rgba(0,0,0,0.25);
  }
  .offer-band {
    height: 74px; background: var(--accent);
    display: flex; align-items: center; justify-content: center;
    font-family: "Montserrat", Arial, sans-serif;
    font-weight: 800; font-size: 35px; letter-spacing: 1px;
    color: var(--headline);
  }

  .link-preview {
    height: 157px; background: var(--link-bg);
    padding: 22px 26px 0; position: relative;
  }
  .link-domain { font-size: 22px; color: var(--text-muted); letter-spacing: 0.5px; }
  .link-title { font-size: 28px; font-weight: 500; margin-top: 10px; }
  .link-subtitle { font-size: 25px; color: var(--text-muted); margin-top: 8px; }
  .call-button {
    position: absolute; right: 40px; top: 44px;
    width: 192px; height: 66px; border-radius: 10px;
    background: var(--button-bg);
    display: flex; align-items: center; justify-content: center; gap: 10px;
    font-size: 26px; font-weight: 500; color: var(--text-main);
  }

  .post-actions {
    flex: 1; border-top: 2px solid var(--divider);
    display: flex; align-items: center; justify-content: space-around;
    padding: 0 30px;
  }
  .action { display: flex; align-items: center; gap: 12px; font-size: 24px; font-weight: 500; color: var(--text-muted); }
</style>
</head>
<body>
  <article class="ad-post">
    <header class="post-header">
      <div class="author">
        <div class="author-avatar"></div>
        <div>
          <div class="author-name">Harlow Moving</div>
          <div class="author-meta">Sponsored</div>
        </div>
      </div>
      <svg class="more-menu" width="36" height="10" viewBox="0 0 36 10" aria-hidden="true">
        <circle cx="5" cy="5" r="4" fill="#606770"/><circle cx="18" cy="5" r="4" fill="#606770"/><circle cx="31" cy="5" r="4" fill="#606770"/>
      </svg>
      <p class="post-text">Harlow Moving also offer Long-Distance Moving Service!</p>
    </header>

    <div class="ad-visual" role="img" aria-label="Aerial photo of a white moving truck driving across a highway bridge with forested hills behind">
      <h1 class="ad-headline">LONG-DISTANCE<br>MOVING SERVICE</h1>
    </div>
    <div class="offer-band">FREE IN-HOUSE QUOTE!</div>

    <section class="link-preview">
      <div class="link-domain">HARLOWMOVE.COM</div>
      <div class="link-title">Free In-House Quote!</div>
      <div class="link-subtitle">For a Peaceful Move</div>
      <div class="call-button">
        <svg width="26" height="26" viewBox="0 0 24 24" aria-hidden="true">
          <path fill="#1c1e21" d="M6.6 10.8a15.1 15.1 0 0 0 6.6 6.6l2.2-2.2a1 1 0 0 1 1-.25 11.4 11.4 0 0 0 3.6.57 1 1 0 0 1 1 1V20a1 1 0 0 1-1 1A17 17 0 0 1 3 4a1 1 0 0 1 1-1h3.5a1 1 0 0 1 1 1c0 1.25.2 2.45.57 3.6a1 1 0 0 1-.25 1z"/>
        </svg>
        Call now
      </div>
    </section>

    <footer class="post-actions">
      <div class="action">
        <svg width="28" height="28" viewBox="0 0 24 24" aria-hidden="true" fill="none" stroke="#65676b" stroke-width="1.8" stroke-linejoin="round">
          <path d="M7 10v11H3V10zM7 10l4-7c1.5 0 2.5 1 2.2 2.6L12.6 9H19a2 2 0 0 1 2 2.3l-1.3 7.4A2 2 0 0 1 17.7 21H7"/>
        </svg>Like
      </div>
      <div class="action">
        <svg width="28" height="28" viewBox="0 0 24 24" aria-hidden="true" fill="none" stroke="#65676b" stroke-width="1.8" stroke-linejoin="round">
          <path d="M4 4h16v12H9l-5 4z"/>
        </svg>Comment
      </div>
      <div class="action">
        <svg width="28" height="28" viewBox="0 0 24 24" aria-hidden="true" fill="none" stroke="#65676b" stroke-width="1.8" stroke-linejoin="round">
          <path d="M14 4l7 7-7 7v-4c-5 0-8 1.5-11 5 1-6 4-10 11-11z"/>
        </svg>Share
      </div>
    </footer>
  </article>
</body>
</html>
```